Medical Marijuana Service in the Bay Area

This is for a business card design that is going to be making medical marijuana deliveries in the bay area. The name of the the business is "Coastal Sage Wellness". I would like to have a modern feel and showing us as a medical marijuana company but at the same time discrete about it. I'm trying to target more sophisticated clients.

Industry/Entity Type

Medical

Contact Information for Business Card

Would like people to know it is for medical marijuana but in a discrete way.

```html
<!DOCTYPE html>
<html lang="en">
<head>
<meta charset="utf-8">
<title>Coastal Sage Wellness — Business Card</title>
<link rel="stylesheet" href="https://fonts.googleapis.com/css2?family=Saira+Extra+Condensed:wght@500&display=swap">
<style>
  :root {
    --card-bg: #fdfdfd;
    --card-shade: #f1f1f1;
    --ink: #5d5d5f;
    --leaf-green: #a6cf45;
  }
  html, body {
    margin: 0;
    padding: 0;
    width: 1200px;
    height: 704px;
    overflow: hidden;
    background: var(--card-bg);
  }
  .card {
    position: relative;
    width: 1200px;
    height: 704px;
    overflow: hidden;
    background: var(--card-bg);
  }
  .card-decor {
    position: absolute;
    inset: 0;
    background: radial-gradient(ellipse 520px 600px at 1010px 560px, var(--card-shade) 0%, rgba(241,241,241,0) 70%);
  }
  .brand-dot {
    position: absolute;
    left: 555px;
    top: 165px;
    width: 90px;
    height: 90px;
  }
  .brand-name {
    position: absolute;
    left: 0;
    top: 331px;
    width: 1200px;
    height: 120px;
    margin: 0;
  }
  .brand-name text {
    font-family: "Saira Extra Condensed", "Arial Narrow", sans-serif;
    font-weight: 500;
    font-size: 104px;
    fill: var(--ink);
  }
</style>
</head>
<body>
  <main class="card">
    <div class="card-decor" role="img" aria-label="Faint oversized herbal mortar and pestle backdrop"></div>
    <svg class="brand-dot" viewBox="0 0 90 90" aria-hidden="true">
      <circle cx="45" cy="45" r="44" fill="var(--leaf-green)"/>
    </svg>
    <h1 class="brand-name">
      <svg viewBox="0 0 1200 120" width="1200" height="120" role="img" aria-label="Coastal Sage Wellness">
        <text x="600" y="88" text-anchor="middle" textLength="775" lengthAdjust="spacingAndGlyphs">Coastal Sage Wellness</text>
      </svg>
    </h1>
  </main>
</body>
</html>
```